Catering free gift mailing

A promotional 2-sided A5 postcode to be posted to new & existing business customers.

We shall be offering a choice of 3 free-gifts to all customers who rent one of these cooking ranges.

Wording is suggestion only, and I am more than happy to allow you to change wording etc to suit your design/approach.

Industry/Entity Type

Cooking

Colors

Designer to choose colors to be used in the design.

Requirements
Must have
• Pictures of the 3 gifts & a clear message that bthese are free to all who rent one of the cookers.
Picture(s) of the range & the price from £71pm
Nice to have
• Our brand colours are red/blue, but this need not be the choice of mailing colours

```html
<!DOCTYPE html>
<html lang="en">
<head>
<meta charset="utf-8">
<title>Hearthline – Rent a Range Free Gift Mailer</title>
<link href="https://fonts.googleapis.com/css2?family=Oswald:wght@400;600;700&family=Roboto+Condensed:wght@400;700&display=swap" rel="stylesheet">
<style>
  :root{
    --red:#e0261f;
    --white:#ffffff;
    --ink:#3a3a3a;
    --rule:#c9c9c9;
    --steel-light:#e4e6e8;
    --steel-dark:#8d9297;
    --backdrop:#d9d9d9;
  }
  *{box-sizing:border-box;margin:0;padding:0}
  html,body{width:1200px;height:891px;overflow:hidden;background:var(--backdrop)}
  .postcard{
    position:absolute;top:247px;width:560px;height:396px;
    background:var(--white);box-shadow:0 4px 14px rgba(0,0,0,.18);
  }
  .postcard--front{left:25px}
  .postcard--back{left:615px}
  .postcard-frame{position:absolute;inset:9px;border:3px solid var(--red)}

  .brand{
    position:absolute;left:22px;top:22px;
    background:var(--red);color:var(--white);
    font:700 14px/1 "Oswald",sans-serif;letter-spacing:.5px;text-transform:uppercase;
    padding:6px 9px;
  }
  .headline{position:absolute;left:24px;top:50px;width:330px;color:var(--red);font-family:"Oswald",sans-serif}
  .headline-top{display:flex;align-items:flex-end;gap:9px}
  .headline-rent{font-weight:700;font-size:54px;line-height:1}
  .headline-sub{font:700 12px/1.15 "Roboto Condensed",sans-serif;text-transform:uppercase;padding-bottom:8px;width:112px}
  .headline-price{font-weight:700;font-size:92px;line-height:.95;letter-spacing:-1px}
  .range-photo{
    position:absolute;left:30px;top:204px;width:230px;height:116px;
    background:linear-gradient(160deg,var(--steel-light),var(--steel-dark));
  }
  .ribbon{
    background:var(--red);color:var(--white);
    font:700 11px/1 "Roboto Condensed",sans-serif;text-transform:uppercase;
    text-align:center;padding:6px 8px;letter-spacing:.3px;white-space:nowrap;
  }
  .ribbon-offer{position:absolute;left:24px;top:334px;width:320px;font-size:12px}
  .gift{position:absolute;left:384px;width:136px;text-align:center}
  .gift-circle{
    width:86px;height:86px;margin:0 auto;border-radius:50%;
    border:3px solid var(--red);overflow:hidden;background:var(--white);
  }
  .gift-photo{width:100%;height:100%}
  .gift-photo--mixer{background:radial-gradient(circle,#d5d8db,#8a9096)}
  .gift-photo--vacuum{background:radial-gradient(circle,#3f7fc4,#1d3f73)}
  .gift-photo--blender{background:radial-gradient(circle,#d5d8db,#7a8086)}
  .gift .ribbon{position:relative;margin-top:-6px;display:block}
  .gift-1{top:26px}.gift-2{top:144px}.gift-3{top:262px}

  .back-divider{position:absolute;left:282px;top:30px;bottom:30px;border-left:1px solid var(--rule)}
  .address-lines{position:absolute;left:302px;top:118px;width:226px;list-style:none}
  .address-lines li{height:34px;border-bottom:1px solid var(--rule)}
  .about{
    position:absolute;left:26px;top:196px;width:238px;height:172px;
    border:3px solid var(--red);padding:30px 12px 10px;
  }
  .about-title{position:absolute;left:-3px;top:-3px;right:-3px;text-align:left;font-size:12px}
  .about-text{font:400 11.5px/1.45 "Roboto Condensed",sans-serif;color:var(--ink)}
</style>
</head>
<body>
  <main class="postcard postcard--front">
    <div class="postcard-frame"></div>
    <div class="brand">Hearthline</div>
    <section class="headline">
      <div class="headline-top">
        <span class="headline-rent">Rent a</span>
        <span class="headline-sub">commercial cooking range from</span>
      </div>
      <div class="headline-price">£71pm</div>
    </section>
    <div class="range-photo" role="img" aria-label="Photograph of a stainless steel commercial cooking range"></div>
    <div class="ribbon ribbon-offer">Choose one free gift when you rent a range today</div>

    <figure class="gift gift-1">
      <div class="gift-circle"><div class="gift-photo gift-photo--mixer" role="img" aria-label="Photograph of a free stand mixer gift"></div></div>
      <figcaption class="ribbon">Free Stand Mixer</figcaption>
    </figure>
    <figure class="gift gift-2">
      <div class="gift-circle"><div class="gift-photo gift-photo--vacuum" role="img" aria-label="Photograph of a free wet and dry vacuum gift"></div></div>
      <figcaption class="ribbon">Free Wet Vacuum</figcaption>
    </figure>
    <figure class="gift gift-3">
      <div class="gift-circle"><div class="gift-photo gift-photo--blender" role="img" aria-label="Photograph of a free food mixer gift"></div></div>
      <figcaption class="ribbon">Free Food Mixer</figcaption>
    </figure>
  </main>

  <section class="postcard postcard--back">
    <div class="back-divider"></div>
    <ul class="address-lines"><li></li><li></li><li></li><li></li><li></li></ul>
    <article class="about">
      <h2 class="ribbon about-title">About us</h2>
      <p class="about-text">Hearthline are commercial catering equipment specialists. We have supplied kitchens across the country for over twenty years, and our rental plans make it simple to upgrade your range without a large upfront cost.</p>
    </article>
  </section>
</body>
</html>
```